2025 Kesto Selvino Truck Hybrid

We are looking to have a wrap designed for our NEW kesto selvino hybrid.
- We want to highlight subtly its a hybrid and green
- We want it to be a partial wrap. Its a white truck so the empty space being white is fine.
- We arent happy with the green in our logo right now. Our other trucks had a richer green and for some reason the graphic designer with our new logo is very pastel and boring.
- See pictures attached of our other trucks. Also the branding guideline colors are NOT right. But i attached it for interest.
We also want a "Now hiring" sign on the back that is subtle.
We want to promote that we do 24/7 Emergancy Service
Website, Socials icons, phone number need to be listed.
We specialize in Construction, Facility Maintenance, Snow & Ice control
All drivers doors need to be equipped with small stickers that have first aid, fire extinguisher and no smoking sign.
We want the wrap to have a similar theme but a new more bold look than our current trucks.
We want to provide this to our Wrap guy for print.
Any ai renderings will be disqualified.

```html
<!DOCTYPE html>
<html lang="en">
<head>
<meta charset="utf-8">
<title>Northvale Contracting – Kesto Selvino Hybrid Partial Wrap</title>
<link rel="stylesheet" href="https://fonts.googleapis.com/css2?family=Montserrat:wght@400;600;700;800&display=swap">
<style>
  :root {
    --wrap-green: #1d6131;
    --wrap-grey: #e2e3e6;
    --brand-grey: #5d5f63;
    --accent-green: #8dbb8f;
    --paper: #ffffff;
  }
  html, body {
    margin: 0;
    width: 1200px;
    height: 1200px;
    overflow: hidden;
    background: var(--paper);
  }
  .wrap-canvas {
    display: block;
    width: 1200px;
    height: 1200px;
    font-family: "Montserrat", sans-serif;
  }
  .headline { font-weight: 700; font-size: 16px; fill: var(--paper); }
  .services { font-weight: 600; font-size: 11.5px; fill: var(--paper); }
  .brand-name { font-weight: 600; font-size: 13px; fill: var(--brand-grey); letter-spacing: 0.5px; }
  .brand-tagline { font-weight: 400; font-size: 7.5px; fill: var(--brand-grey); letter-spacing: 1.6px; }
  .phone { font-weight: 800; font-size: 22px; fill: var(--wrap-green); }
  .website { font-weight: 700; font-size: 11px; fill: var(--wrap-green); }
</style>
</head>
<body>
<svg class="wrap-canvas" viewBox="0 0 1200 1200" xmlns="http://www.w3.org/2000/svg" role="img" aria-label="Partial wrap layout for the driver side of the Kesto Selvino hybrid truck">

  <!-- rear panel: main green field with wheel arch opening -->
  <path class="panel-green" fill="var(--wrap-green)"
        d="M105,625 L395,625 L412,583 L580,787 L395,787 L380,770
           C372,722 340,700 300,700 C262,700 232,718 222,745 L215,770
           L165,757 L105,720 Z"/>

  <!-- diagonal accent stripes -->
  <path class="stripe-green" fill="var(--wrap-green)"
        d="M427,583 L442,583 L612,787 L597,787 Z"/>
  <path class="stripe-grey" fill="var(--wrap-grey)"
        d="M470,660 L497,660 L605,787 L578,787 Z"/>

  <!-- rear messaging -->
  <text class="headline" x="287" y="652" text-anchor="middle">24/7 EMERGENCY SERVICE</text>
  <rect x="173" y="656" width="228" height="1.6" fill="var(--paper)"/>
  <text class="services" x="287" y="672" text-anchor="middle">Construction | Facility Maintenance</text>
  <text class="services" x="287" y="684" text-anchor="middle">Snow &amp; Ice control</text>

  <!-- social media placeholders -->
  <g class="social-dots" fill="var(--paper)">
    <circle cx="461" cy="754" r="12"/>
    <circle cx="490" cy="754" r="12"/>
    <circle cx="519" cy="754" r="12"/>
  </g>

  <!-- door safety sticker strip -->
  <g class="safety-stickers">
    <rect x="733" y="646" width="37" height="13" rx="1.5" fill="none" stroke="var(--wrap-green)" stroke-width="1.4"/>
    <circle cx="741" cy="652.5" r="4" fill="var(--wrap-green)"/>
    <circle cx="751.5" cy="652.5" r="4" fill="none" stroke="var(--wrap-green)" stroke-width="1.2"/>
    <circle cx="762" cy="652.5" r="4" fill="none" stroke="var(--wrap-green)" stroke-width="1.2"/>
  </g>

  <!-- brand name -->
  <g class="brand-lockup">
    <circle cx="556" cy="694" r="7" fill="var(--accent-green)"/>
    <text class="brand-name" x="776" y="699" text-anchor="end">NORTHVALE CONTRACTING</text>
    <text class="brand-tagline" x="776" y="714" text-anchor="end">BUILT ON GOOD PEOPLE</text>
  </g>

  <!-- contact -->
  <text class="phone" x="614" y="763">555-014-2290</text>
  <text class="website" x="615" y="777">Northvalecontracting.com</text>
</svg>
</body>
</html>
```